Company or website name
- spinthevelvetloop.com
- Links to the website
- I am a DJ, this site will be used strictly a place where I will post new mixes I have done, sort of like a running blog and you will be able to listen to the most recent mix I posted or download, you will see artwork for the mix along with tracklist
- Other Facts

```html
<!DOCTYPE html>
<html lang="en">
<head>
<meta charset="utf-8">
<title>spinthevelvetloop.com</title>
<link rel="stylesheet" href="https://fonts.googleapis.com/css2?family=Arimo:wght@400;700&family=Archivo+Narrow:wght@400;600&family=Archivo+Black&display=swap">
<style>
  :root {
    --page-dark: #141414;
    --page-mid: #2b2b2b;
    --panel: #e4e4e4;
    --panel-light: #f1f1f1;
    --nav-top: #d9d9d9;
    --nav-bottom: #bdbdbd;
    --tab: #e9e9e9;
    --ink: #111111;
    --muted: #a6a6a6;
    --accent: #8c0b0b;
    --accent-bright: #a80f0f;
    --white: #ffffff;
  }
  * { box-sizing: border-box; margin: 0; padding: 0; }
  html, body { width: 1200px; height: 1200px; overflow: hidden; }
  body {
    background: radial-gradient(ellipse at 50% 40%, var(--page-mid), var(--page-dark) 75%);
    font-family: "Arimo", Arial, sans-serif;
    color: var(--ink);
  }
  .stage {
    position: absolute; left: 0; top: 0;
    width: 1020px; height: 1020px;
    transform: scale(1.17647); transform-origin: 0 0;
  }
  .abs { position: absolute; }

  .site-name {
    left: 40px; top: 28px;
    font-family: "Arimo", Arial, sans-serif; font-weight: 700;
    font-size: 30px; color: var(--white); letter-spacing: -0.5px;
  }
  .search {
    left: 778px; top: 36px; width: 202px; height: 26px;
    background: #262626; border: 1px solid #8a8a8a;
    display: flex; align-items: center;
  }
  .search-field { flex: 1; padding-left: 6px; font-size: 10px; color: #e0e0e0; }
  .search-go {
    width: 20px; height: 18px; margin-right: 4px;
    background: #cfcfcf; color: #222; font-size: 9px;
    display: flex; align-items: center; justify-content: center;
  }

  .panel {
    left: 40px; top: 70px; width: 940px; height: 870px;
    background: linear-gradient(180deg, #e6e6e6, #d8d8d8);
    box-shadow: 0 0 12px rgba(0,0,0,.6);
  }
  .nav {
    left: 40px; top: 70px; width: 940px; height: 48px;
    background: linear-gradient(180deg, var(--nav-top), var(--nav-bottom));
  }
  .nav-tab {
    top: 79px; height: 27px;
    background: linear-gradient(180deg, #f2f2f2, #d4d4d4);
    box-shadow: 1px 1px 2px rgba(0,0,0,.35);
    font-family: "Archivo Black", Arial, sans-serif;
    font-size: 12px; letter-spacing: .5px; color: #1d1d1d;
    display: flex; align-items: center; justify-content: center;
  }
  .nav-date {
    left: 780px; top: 84px; width: 174px; text-align: right;
    font-weight: 700; font-size: 16px; color: var(--muted);
  }

  .hero-art {
    left: 40px; top: 118px; width: 575px; height: 178px;
    background: linear-gradient(90deg, #9a9a9a, #c9c9c9 35%, #a53535 52%, #bdbdbd 65%, #5a5a5a 90%);
  }
  .hero-copy {
    left: 615px; top: 118px; width: 365px; height: 178px;
    background: linear-gradient(180deg, #b9b9b9, #d3d3d3);
  }
  .hero-title {
    left: 647px; top: 128px;
    font-family: "Archivo Narrow", Arial, sans-serif; font-weight: 600;
    font-size: 18px; color: var(--accent);
  }
  .hero-text {
    left: 647px; top: 162px; width: 306px;
    font-size: 11px; line-height: 17px; color: #1a1a1a;
  }
  .signup {
    left: 866px; top: 252px; width: 83px; height: 31px;
    background: var(--accent-bright); color: var(--white);
    font-family: "Archivo Narrow", Arial, sans-serif; font-size: 15px;
    display: flex; align-items: center; justify-content: center;
    box-shadow: 1px 1px 3px rgba(0,0,0,.4);
  }
  .hero-rule { left: 40px; top: 296px; width: 940px; height: 3px; background: #a9a9a9; }

  .ads { left: 72px; top: 303px; font-size: 11px; letter-spacing: .4px; }
  .ads b { font-weight: 700; }

  .main-col {
    left: 40px; top: 322px; width: 608px; height: 618px;
    background: linear-gradient(180deg, #e9e9e9, var(--panel-light) 40%, #ececec);
    border-right: 2px solid #c8c8c8;
  }
  .post-frame {
    left: 110px; top: 350px; width: 459px; height: 346px;
    background: var(--white); box-shadow: 2px 3px 5px rgba(0,0,0,.35);
  }
  .post-art {
    left: 122px; top: 358px; width: 435px; height: 330px;
    background: radial-gradient(ellipse at 45% 45%, #b50f0f, #8f0a0a 80%);
  }
  .post-title {
    left: 70px; top: 721px;
    font-family: "Archivo Narrow", Arial, sans-serif; font-weight: 600;
    font-size: 18px; color: var(--accent);
  }
  .post-text {
    left: 70px; top: 755px; width: 540px;
    font-size: 11px; line-height: 17px; color: #1a1a1a;
  }
  .read-more { color: var(--accent); margin-left: 20px; }
  .comments { left: 470px; top: 815px; width: 138px; text-align: right; font-size: 14px; color: var(--accent); }
  .share { top: 840px; width: 32px; height: 32px; }

  .sidebar-title {
    left: 660px; top: 320px; width: 293px; text-align: center;
    font-size: 17px; color: var(--accent-bright); letter-spacing: .5px;
  }
  .sidebar-rule { left: 660px; top: 341px; width: 293px; height: 2px; background: #3a3a3a; }
  .blogroll {
    left: 660px; top: 356px; width: 293px; text-align: right;
    list-style: none; font-size: 17px; line-height: 21px; color: var(--ink);
  }
</style>
</head>
<body>
<div class="stage">
  <header>
    <div class="abs site-name">SpinTheVelvetLoop</div>
    <div class="abs search"><span class="search-field">SEARCH ...</span><span class="search-go">GO</span></div>
  </header>

  <div class="abs panel"></div>

  <nav>
    <div class="abs nav"></div>
    <div class="abs nav-tab" style="left:72px;width:73px">ABOUT</div>
    <div class="abs nav-tab" style="left:168px;width:90px">DOWNLOAD</div>
    <div class="abs nav-tab" style="left:283px;width:90px">ARCHIVES</div>
    <div class="abs nav-tab" style="left:411px;width:78px">LINKAGE</div>
    <div class="abs nav-tab" style="left:526px;width:78px">CONTACT</div>
    <div class="abs nav-date">Thursday, May 13</div>
  </nav>

  <section class="hero">
    <div class="abs hero-art" role="img" aria-label="Illustration of a DJ in a red shirt at turntables beside a mixer"></div>
    <div class="abs hero-copy"></div>
    <h2 class="abs hero-title">Lorem Ipsum Dolor sit Amet</h2>
    <p class="abs hero-text">just simplydummytexts in printing industries just simply dummytexts in printing industries just simplydummytexts in printing industries just simply dummytexts in printing industries just simplydummytexts in printing industries just simplydummytexts in printing industries just simplydummy texts in printing industries</p>
    <div class="abs signup">SIGN UP</div>
    <div class="abs hero-rule"></div>
  </section>

  <div class="abs ads"><b>Ads by Adnetwork</b> : AdSpace $$$ place here ...</div>

  <main>
    <div class="abs main-col"></div>
    <div class="abs post-frame"></div>
    <div class="abs post-art" role="img" aria-label="Red mix artwork for the latest post"></div>
    <h2 class="abs post-title">Lorem Ipsum Dolor sit Amet</h2>
    <p class="abs post-text">just simplydummytexts in printing industries just simplydummytexts in printing industries just simply dummytexts in printing industries just simplydummytexts in printing industries just simplydummytexts in printing industries just simplydummytexts in printing industries just simplydummytexts in printing indus-tries... <span class="read-more">Read More &gt;</span></p>
    <div class="abs comments">46 Comments</div>

    <svg class="abs share" style="left:72px" viewBox="0 0 32 32" role="img" aria-label="Share"><rect x="1" y="1" width="30" height="30" rx="5" fill="#3d3d3d"/></svg>
    <svg class="abs share" style="left:122px" viewBox="0 0 32 32" role="img" aria-label="Share"><rect x="1" y="1" width="30" height="30" rx="5" fill="#6cc4e6"/></svg>
    <svg class="abs share" style="left:173px" viewBox="0 0 32 32" role="img" aria-label="Share"><rect x="1" y="1" width="30" height="30" rx="5" fill="#2f8f3a"/></svg>
    <svg class="abs share" style="left:223px" viewBox="0 0 32 32" role="img" aria-label="Share"><rect x="1" y="1" width="30" height="30" rx="5" fill="#8ea4b3"/></svg>
    <svg class="abs share" style="left:274px" viewBox="0 0 32 32" role="img" aria-label="Share"><rect x="1" y="1" width="30" height="30" rx="5" fill="#3b5c9c"/></svg>
    <svg class="abs share" style="left:324px" viewBox="0 0 32 32" role="img" aria-label="Feed"><rect x="1" y="1" width="30" height="30" rx="5" fill="#ef8a24"/></svg>
  </main>

  <aside>
    <h3 class="abs sidebar-title">BLOG ROLL</h3>
    <div class="abs sidebar-rule"></div>
    <ul class="abs blogroll">
      <li>Hiphop</li>
      <li>Dub</li>
      <li>...</li>
    </ul>
  </aside>
</div>
</body>
</html>
```